Progressive European Honey Business needs minimalistic packaging design

Hello - thank you for your interest in our brief. We are Velvet Jinx, a London based Honey business, importing only the best honey Europe has to offer. Our values are deeply rooted with in progressive liberal values and we are looking for minimalist packaging, which reflects that.

We are looking for a design, which dimensions fit with our packaging option (Kelmor Glass Jar | HEIGHT 90mm | DIAMETER 63mm). We will require a various output files (High Resolution JPEG (CMYK Colors 300 dpi) Source File Ai, PSD, PDF, Printing files (die cut, die folding) and a 3D Mockup of the packaging for use within digital commerce platforms.

We must be able to adjust the free text on the label front and it should include the following:
Brand Name
Honey type
Limited edition No. X / 100 ( X being the number of purchase i.e. 25 / 100)
EU Honey, Single Orgin (Germany)
(c) The net weight (250g)

The back must include room for additional information (again adjustable by us) and the following:
“Unsuitable for children under 12 months”
(b) The appropriate durability declaration

In total, we are looking for
a) A front label
b) A back label
c) A seal (round) including the attached bee and logo included in the Zip file.
Do note that a) & b) can also be combined into one design as long as the symmetry on the jar stays intact.

The final design should communicate modern aesthetics, high quality, that are slightly provocative and pop off the shelves.
Updates

Hi folks, sorry for the delay in completing this project, but my business partner had a leak in his house. We planned to finalise our review today, but this will have to wait until it's no longer raining in his livingroom. Our sincere apologies!

Other font styles liked:
• See branding guidelines

Requirements
Must have
• Must follow the branding guideline and fonts provided as attachment

```html
<!DOCTYPE html>
<html lang="en">
<head>
<meta charset="utf-8">
<title>Velvet Jinx – Raw Honey Label</title>
<link rel="stylesheet" href="https://fonts.googleapis.com/css2?family=Lato:wght@400;900&display=swap">
<style>
  :root {
    --paper: #ffffff;
    --ink: #2f2f2f;
    --band-dark-a: #6a5f52;
    --band-dark-b: #2e2a26;
    --gold-a: #e9cf5a;
    --gold-b: #f1de74;
    --gold-edge: #d4a93a;
    --label-text: #f0dd6e;
  }
  html, body {
    margin: 0;
    padding: 0;
    width: 1014px;
    height: 1200px;
    overflow: hidden;
    background: var(--paper);
  }
  .label-canvas {
    display: block;
    width: 1014px;
    height: 1200px;
  }
  .brand-name {
    font-family: "Lato", sans-serif;
    font-weight: 900;
    font-size: 60px;
    fill: var(--ink);
  }
  .variety {
    font-family: "Lato", sans-serif;
    font-weight: 400;
    font-size: 44px;
    fill: var(--label-text);
  }
  .origin {
    font-family: "Lato", sans-serif;
    font-weight: 400;
    font-size: 34px;
    fill: var(--ink);
  }
  .side-text {
    font-family: "Lato", sans-serif;
    font-weight: 400;
    font-size: 24px;
    fill: var(--ink);
  }
  .side-rule {
    stroke: var(--ink);
    stroke-width: 3;
  }
</style>
</head>
<body>
<svg class="label-canvas" viewBox="0 0 1014 1200" xmlns="http://www.w3.org/2000/svg">
  <defs>
    <linearGradient id="band-dark" x1="0" y1="0" x2="1" y2="0">
      <stop offset="0" stop-color="var(--band-dark-a)"/>
      <stop offset="1" stop-color="var(--band-dark-b)"/>
    </linearGradient>
    <linearGradient id="band-gold" x1="0" y1="0" x2="1" y2="0">
      <stop offset="0" stop-color="var(--gold-b)"/>
      <stop offset="0.5" stop-color="var(--gold-a)"/>
      <stop offset="1" stop-color="var(--gold-b)"/>
    </linearGradient>
    <linearGradient id="hex-gold" x1="0" y1="0" x2="1" y2="1">
      <stop offset="0" stop-color="var(--gold-a)"/>
      <stop offset="1" stop-color="var(--gold-b)"/>
    </linearGradient>
  </defs>

  <!-- wrap band: patterned top strip -->
  <rect class="band-pattern" x="27" y="440" width="960" height="220" fill="url(#band-dark)"
        role="img" aria-label="Dark honeycomb pattern strip"/>
  <!-- wrap band: gold lower strip -->
  <rect class="band-gold" x="27" y="655" width="960" height="245" fill="url(#band-gold)"/>

  <!-- side information, left -->
  <g class="side-info side-info--left">
    <text class="side-text" x="50" y="705">Limited edition</text>
    <line class="side-rule" x1="50" y1="745" x2="220" y2="745"/>
    <text class="side-text" x="50" y="795">No. 25 / 100</text>
  </g>

  <!-- side information, right -->
  <g class="side-info side-info--right">
    <text class="side-text" x="964" y="705" text-anchor="end">Net weight</text>
    <line class="side-rule" x1="794" y1="745" x2="964" y2="745"/>
    <text class="side-text" x="964" y="795" text-anchor="end">250 g</text>
  </g>

  <!-- central hexagon badge -->
  <g class="hex-badge">
    <polygon points="372,392 642,392 756,680 642,968 372,968 258,680"
             fill="var(--gold-edge)"/>
    <polygon points="376,400 638,400 748,680 638,960 376,960 266,680"
             fill="var(--ink)"/>
    <polygon points="392,440 622,440 716,680 622,920 392,920 298,680"
             fill="url(#hex-gold)"/>
    <rect class="variety-bar" x="282" y="645" width="450" height="95" fill="var(--ink)"/>

    <text class="brand-name" x="507" y="552" text-anchor="middle">VELVET</text>
    <text class="brand-name" x="507" y="620" text-anchor="middle">JINX</text>

    <text class="variety" x="507" y="708" text-anchor="middle">RAW HONEY</text>

    <text class="origin" x="507" y="800" text-anchor="middle">EU HONEY</text>
    <text class="origin" x="507" y="842" text-anchor="middle">SINGLE ORGIN</text>
  </g>
</svg>
</body>
</html>
```